CFO services graphic design

I own a business consulting firm called Marlowe Consulting and we need a graphic for CFO services in our colours and branding. The attached file "CFO services to be put into Marlowe consulting theme", shows the content for the design. The two other files show the theme and colours for the new design.

```html
<!DOCTYPE html>
<html lang="en">
<head>
<meta charset="UTF-8">
<title>Marlowe Consulting – Chief Financial Officer Services</title>
<link href="https://fonts.googleapis.com/css2?family=Open+Sans:wght@400;700;800&display=swap" rel="stylesheet">
<style>
  :root {
    --brand-gold: #d99a1e;
    --brand-gold-soft: #f2d28c;
    --brand-teal: #12808f;
    --brand-teal-soft: #93d2d9;
    --brand-navy: #1d2b40;
    --hub: #f1f3f5;
    --paper: #ffffff;
  }
  html, body {
    margin: 0;
    padding: 0;
    overflow: hidden;
    background: var(--paper);
  }
  .canvas {
    position: relative;
    width: 1200px;
    height: 1000px;
    overflow: hidden;
    background: var(--paper);
    font-family: "Open Sans", Arial, sans-serif;
    color: var(--brand-navy);
  }
  .wheel {
    position: absolute;
    inset: 0;
  }
  .frame-gold { fill: var(--paper); stroke: var(--brand-gold); stroke-width: 9; stroke-linejoin: round; }
  .frame-teal { fill: var(--paper); stroke: var(--brand-teal); stroke-width: 9; stroke-linejoin: round; }
  .petal-gold { fill: var(--brand-gold-soft); stroke: var(--brand-gold-soft); stroke-width: 16; stroke-linejoin: round; }
  .petal-teal { fill: var(--brand-teal-soft); stroke: var(--brand-teal-soft); stroke-width: 16; stroke-linejoin: round; }
  .hub-face { fill: var(--hub); }
  .hub-arc-gold { fill: none; stroke: var(--brand-gold); stroke-width: 8; stroke-linecap: round; }
  .hub-arc-teal { fill: none; stroke: var(--brand-teal); stroke-width: 8; stroke-linecap: round; }
  .hub-title {
    position: absolute;
    left: 490px;
    top: 443px;
    width: 220px;
    text-align: center;
    font-weight: 800;
    font-size: 30px;
    line-height: 37px;
    letter-spacing: 0.5px;
    color: var(--brand-navy);
  }
  .role {
    position: absolute;
    width: 240px;
    transform: translate(-50%, -50%);
    text-align: center;
    font-weight: 700;
    font-size: 17px;
    line-height: 22px;
    color: var(--brand-navy);
  }
  .role .detail {
    display: block;
    font-weight: 400;
  }
  .brand {
    position: absolute;
    left: 0;
    right: 0;
    top: 952px;
    display: flex;
    justify-content: center;
    align-items: center;
    gap: 10px;
    font-weight: 700;
    font-size: 18px;
    letter-spacing: 1px;
    color: var(--brand-navy);
  }
  .brand-dot {
    width: 12px;
    height: 12px;
    border-radius: 50%;
    background: var(--brand-teal);
  }
</style>
</head>
<body>
<div class="canvas">
  <svg class="wheel" width="1200" height="1000" viewBox="0 0 1200 1000" aria-hidden="true">
    <defs>
      <path id="frame" d="M555.2 380.3 L446.6 97.4 A428 428 0 0 1 753.4 97.4 L644.8 380.3 A125 125 0 0 0 555.2 380.3 Z"/>
      <path id="petal" d="M556 369.4 L470.4 120.7 A398 398 0 0 1 729.6 120.7 L644 369.4 A135 135 0 0 0 556 369.4 Z"/>
      <filter id="hub-shadow" x="-30%" y="-30%" width="160%" height="160%">
        <feDropShadow dx="0" dy="4" stdDeviation="8" flood-color="#000" flood-opacity="0.28"/>
      </filter>
    </defs>

    <g class="segments">
      <use href="#frame" class="frame-gold" transform="rotate(0 600 497)"/>
      <use href="#petal" class="petal-gold" transform="rotate(0 600 497)"/>
      <use href="#frame" class="frame-teal" transform="rotate(45 600 497)"/>
      <use href="#petal" class="petal-teal" transform="rotate(45 600 497)"/>
      <use href="#frame" class="frame-gold" transform="rotate(90 600 497)"/>
      <use href="#petal" class="petal-gold" transform="rotate(90 600 497)"/>
      <use href="#frame" class="frame-teal" transform="rotate(135 600 497)"/>
      <use href="#petal" class="petal-teal" transform="rotate(135 600 497)"/>
      <use href="#frame" class="frame-gold" transform="rotate(180 600 497)"/>
      <use href="#petal" class="petal-gold" transform="rotate(180 600 497)"/>
      <use href="#frame" class="frame-teal" transform="rotate(225 600 497)"/>
      <use href="#petal" class="petal-teal" transform="rotate(225 600 497)"/>
      <use href="#frame" class="frame-gold" transform="rotate(270 600 497)"/>
      <use href="#petal" class="petal-gold" transform="rotate(270 600 497)"/>
      <use href="#frame" class="frame-teal" transform="rotate(315 600 497)"/>
      <use href="#petal" class="petal-teal" transform="rotate(315 600 497)"/>
    </g>

    <g class="hub">
      <circle class="hub-face" cx="600" cy="497" r="128" filter="url(#hub-shadow)"/>
      <path class="hub-arc-gold" d="M497 470 A106 106 0 0 1 703 470"/>
      <path class="hub-arc-teal" d="M703 524 A106 106 0 0 1 497 524"/>
    </g>
  </svg>

  <div class="hub-title">CHIEF<br>FINANCIAL<br>OFFICER</div>

  <div class="role" style="left:602px; top:196px;">Cost Accounting &amp;<br>Cost Management</div>
  <div class="role" style="left:824px; top:296px;">Capital Structure &amp;<br>The Cost of Capital</div>
  <div class="role" style="left:865px; top:503px;">Long-term &amp; Short-term<br>Investment Decisions</div>
  <div class="role" style="left:802px; top:706px;">Performance<br>Evaluation</div>
  <div class="role" style="left:597px; top:806px;">Budgeting &amp;<br>Strategic Planning</div>
  <div class="role" style="left:395px; top:701px;">Risk<br>Management</div>
  <div class="role" style="left:332px; top:496px;">Compliance:<br>Tax, Legal and<br>Regulator</div>
  <div class="role" style="left:388px; top:292px;">Communication:
    <span class="detail">Board of Directors,<br>Creditors, Owners,<br>Investors, Credit Rating<br>Agencies</span>
  </div>

  <div class="brand"><span class="brand-dot"></span>Marlowe Consulting</div>
</div>
</body>
</html>
```